A billboard for Harlow Ridge Construction size 36.5’ x 14.5’

Hi guys. We are purchasing a billboard and are looking for a design (size 36.5’ x 14.5’). Our slogan is "Quality you deserve, service you can count on". The goal of this billboard is brand recognition primarily letting people know we do roofs. Attached are logos that can be used if needed. Not necessarily all of them need to be used.

Target Market(s)

Residents in the local areas needing or thinking about a roof replacement

Industry/Entity Type

Roofing

Requirements
Must have
• Logo and services (roof replacement, gutters, siding, and snow removal)
Nice to have
• take a look at our website for ideas www.harlowridgeconstruction.example

```html
<!DOCTYPE html>
<html lang="en">
<head>
<meta charset="UTF-8">
<title>Harlow Ridge Construction Billboard</title>
<link href="https://fonts.googleapis.com/css2?family=Oswald:wght@500;700&display=swap" rel="stylesheet">
<style>
  :root {
    --canvas-bg: #eef0f3;
    --ink-black: #000000;
    --paper-white: #ffffff;
    --brand-red: #ee0000;
    --sky: #8fb9e2;
    --roof: #a37850;
    --brick: #8a5a44;
    --lawn: #4f8a33;
    --strip-dark: rgba(0, 0, 0, 0.82);
  }
  html, body {
    margin: 0;
    padding: 0;
    width: 1200px;
    height: 1129px;
    overflow: hidden;
    background: var(--canvas-bg);
  }
  .billboard {
    position: absolute;
    left: 0;
    top: 326px;
    width: 1200px;
    height: 477px;
    display: block;
  }
  .headline, .tagline, .phone-number, .brand-name, .services-list {
    font-family: "Oswald", "Arial Narrow", sans-serif;
    font-weight: 700;
  }
  .headline { fill: var(--brand-red); }
  .tagline { fill: var(--paper-white); font-weight: 500; }
  .phone-number { fill: var(--ink-black); font-weight: 500; }
  .brand-name { fill: var(--ink-black); }
  .brand-plate { fill: var(--paper-white); }
  .brand-square { fill: var(--brand-red); }
  .services-strip { fill: var(--strip-dark); }
  .services-list { fill: var(--paper-white); font-weight: 500; }
  .panel-white { fill: var(--paper-white); }
  .panel-black { fill: var(--ink-black); }
  .phone-badge { fill: var(--brand-red); }
  .phone-glyph { fill: var(--paper-white); }
  .phone-waves { fill: none; stroke: var(--paper-white); stroke-width: 7; stroke-linecap: round; }
  .sky-stop { stop-color: var(--sky); }
  .roof-stop { stop-color: var(--roof); }
  .brick-stop { stop-color: var(--brick); }
  .lawn-stop { stop-color: var(--lawn); }
</style>
</head>
<body>
<svg class="billboard" viewBox="0 0 1988 791" xmlns="http://www.w3.org/2000/svg">
  <defs>
    <linearGradient id="house-photo-tones" x1="0" y1="0" x2="0" y2="1">
      <stop offset="0" class="sky-stop"/>
      <stop offset="0.3" class="sky-stop"/>
      <stop offset="0.45" class="roof-stop"/>
      <stop offset="0.68" class="brick-stop"/>
      <stop offset="0.85" class="lawn-stop"/>
      <stop offset="1" class="lawn-stop"/>
    </linearGradient>
  </defs>

  <rect class="panel-white" x="0" y="0" width="1988" height="791"/>

  <polygon class="house-photo" role="img"
           aria-label="Photo of a brick house with a new brown shingle roof and a two-car garage"
           fill="url(#house-photo-tones)"
           points="0,0 835,0 1005,307 730,791 0,791"/>

  <g class="brand-label">
    <rect class="brand-plate" x="30" y="30" width="560" height="92" rx="6"/>
    <rect class="brand-square" x="52" y="51" width="50" height="50"/>
    <text class="brand-name" x="122" y="96" font-size="46" textLength="444" lengthAdjust="spacingAndGlyphs">HARLOW RIDGE CONSTRUCTION</text>
  </g>

  <g class="services">
    <polygon class="services-strip" points="0,712 775,712 730,791 0,791"/>
    <text class="services-list" x="30" y="765" font-size="38" textLength="690" lengthAdjust="spacingAndGlyphs">ROOF REPLACEMENT • GUTTERS • SIDING • SNOW REMOVAL</text>
  </g>

  <polygon class="panel-black" points="870,0 1988,0 1988,585 885,585 1045,307"/>

  <text class="headline headline-main" x="1128" y="255" font-size="260" textLength="797" lengthAdjust="spacingAndGlyphs">QUALITY</text>
  <text class="headline headline-sub" x="1115" y="427" font-size="152" textLength="812" lengthAdjust="spacingAndGlyphs">YOU DESERVE,</text>
  <text class="tagline" x="1068" y="525" font-size="84" textLength="857" lengthAdjust="spacingAndGlyphs">SERVICE YOU CAN COUNT ON</text>

  <g class="phone-icon" transform="translate(1007,678)">
    <circle class="phone-badge" r="66"/>
    <path class="phone-glyph" d="M-34,-30 C-38,-22 -36,-8 -24,10 C-12,28 4,40 18,44 C26,46 34,40 38,32 L26,18 C22,14 16,16 12,22 C0,16 -10,4 -16,-10 C-10,-14 -8,-20 -12,-24 L-24,-36 C-28,-38 -32,-34 -34,-30 Z"/>
    <path class="phone-waves" d="M2,-26 A26,26 0 0 1 26,-2"/>
    <path class="phone-waves" d="M4,-44 A44,44 0 0 1 44,-4"/>
  </g>

  <text class="phone-number" x="1118" y="732" font-size="150" textLength="808" lengthAdjust="spacingAndGlyphs">262-555-0148</text>
</svg>
</body>
</html>
```